Fine Art business needs new website

We need a simple website with a home page, about us page, New sculptures, Sold sculptures, and a contact us page.Our sculptures are very high end one of a kind pieces. As such we need the site to be VERY elegant and professional. Lastly, because I'll be updating pictures on the website on a monthly basis it needs to be user friendly to update (Wordpress is preferred). The only branding we have so far for the business is a business card.
Updates
I wasn't completely ready when this project launched, also I am on the road right now and haven't been able to be as responsive to all you designers as I would like. I will work on giving feedback to all the top designs we've received so far. Thank you all so much for your participation and hardwork.
Target Market(s)
High end customers (affluent), art collectors, interior decorators/designers
Industry/Entity Type
Art Gallery
Coding
Coded - Design and coding required
Number of Pages Required
5+ page
Requirements
Must have
- Easily editable picture gallery for myself so that I can add new pieces(pictures of the pieces), remove sold pieces, etc. I would like the website to be built in wordpress so I can update it. I currently use tendsitehub through Hostwick for my other business website and would like to do the same for this one.
- Pages:
- -Intro page with featured pieces
- -Current pieces gallery (for sale) mainly a picture gallery
- -Sculptures archive (sold pieces) another picture gallery
- -About us: Pull-down of -about the artist (attached content)
- -Artistic Process (attached content)
- -Show Schedule:
- -one page dedicated to "friends of OKW" (basically a link page)
- TO BE CLEAR "www.brindlelads.example" IS A TOTALLY DIFFERENT SITE AND I'M NOT TRYING TO COMBINE THE TWO OR JOIN THEM INTO ONE. This page needs be more elegant and seperate from The Brindle Lads site.
- UPDATE: I'd like a link to the OKW Chatterly page: https://www.chatterly.example/orvanekilnworks/
Nice to have
- I would like the pictures on the gallery pages able to have text connected with them (Materials, price)
- I would like the site style and fonts to be similar to our business cards we've already had designed (picture attached).
Should not have
- Too much flash or other things that will make the site slow to load.

```html
<!DOCTYPE html>
<html lang="en">
<head>
<meta charset="utf-8">
<title>Orvane Kiln Works</title>
<link rel="stylesheet" href="https://fonts.googleapis.com/css2?family=Montserrat:wght@400;500;600;700&family=Cormorant+Garamond:wght@400;500&family=Poppins:wght@400;500&display=swap">
<style>
:root{
  --ink:#1d1d1f;
  --text:#555;
  --muted:#8a8a8a;
  --line:#d9d9d9;
  --band:#f7f7f7;
  --tag:#e6e6e6;
  --dark:#151515;
  --button:#262b33;
  --white:#fff;
}
*{margin:0;padding:0;box-sizing:border-box}
html,body{width:1200px;height:3442px;overflow:hidden;background:var(--white)}
body{position:relative;font-family:"Montserrat",sans-serif;color:var(--ink)}
.abs{position:absolute}
.logo{left:57px;top:36px;font-family:"Cormorant Garamond",serif;font-size:22px;letter-spacing:2px;color:var(--ink)}
.nav{top:42px;font-size:9.5px;font-weight:500;letter-spacing:1px;text-transform:uppercase}
.nav-tools{left:1132px;top:38px;display:flex;gap:8px}
.hero{left:418px;top:85px;width:782px;height:367px;background:radial-gradient(ellipse at 50% 40%,#5a3f86 0%,#2a1e3b 18%,#111 45%)}
.tagline{left:57px;top:204px;font-size:14px;font-weight:500}
.hero-title{left:57px;top:232px;font-size:31px;font-weight:700;letter-spacing:7px}
.slider-lines{left:60px;top:326px;display:flex;gap:6px}
.slider-lines span{width:26px;height:2px;background:#ccc}
.slider-lines span:first-child{background:#eee}
.section-title{width:100%;text-align:center;font-size:38px;font-weight:700;letter-spacing:11px}
.subline{left:635px;top:587px;width:90px;height:1px;background:var(--ink)}
.subtag{left:730px;top:578px;width:346px;height:20px;background:var(--tag);font-size:12px;letter-spacing:1px;padding:3px 6px;color:var(--text)}
.piece{background:var(--dark)}
.p-green{background:linear-gradient(90deg,#141414 40%,#5f9b7d 48%,#2f6a4e 54%,#141414 62%)}
.p-malachite{background:radial-gradient(ellipse at 50% 45%,#2e8e6a 0%,#11553d 25%,#121212 50%)}
.p-blue{background:radial-gradient(ellipse at 50% 50%,#6f78b8 0%,#3b3f66 28%,#121212 55%)}
.p-agate{background:radial-gradient(ellipse at 45% 50%,#b86a2a 0%,#5b3315 22%,#141414 45%)}
.p-lace{background:radial-gradient(ellipse at 50% 50%,#a9c1d8 0%,#52687e 25%,#141414 50%)}
.p-ammonite{background:radial-gradient(ellipse at 50% 50%,#a0774d 0%,#5e4127 28%,#141414 55%)}
.p-coral{background:radial-gradient(ellipse at 60% 50%,#d9c6a4 0%,#7d6a4e 26%,#141414 52%)}
.p-thumb-a{background:radial-gradient(circle,#7a6152 0%,#1b1b1b 60%)}
.p-thumb-b{background:radial-gradient(circle,#cdbd9d 0%,#1b1b1b 60%)}
.p-thumb-c{background:radial-gradient(circle,#5c3f8f 0%,#1b1b1b 60%)}
.p-thumb-d{background:radial-gradient(circle,#c49a3c 0%,#1b1b1b 60%)}
.p-thumb-e{background:#2a2a2a}
.p-thumb-f{background:radial-gradient(circle,#6a4aa6 0%,#1b1b1b 60%)}
.more{display:flex;align-items:center;justify-content:center}
.gallery-arrows{left:941px;top:1579px;display:flex;gap:16px}
.feature{left:96px;top:1801px;width:704px;height:337px;background:radial-gradient(ellipse at 50% 50%,#6d52a8 0%,#4a3578 35%,rgba(255,255,255,0) 70%)}
.about-title{left:833px;top:1855px;font-size:31px;font-weight:700;letter-spacing:6px}
.about-copy{left:833px;top:1928px;width:265px;font-size:9.5px;line-height:25px;color:var(--text)}
.band{left:0;top:2276px;width:1200px;height:436px;background:var(--band)}
.quote-card{left:369px;top:2276px;width:468px;height:257px;background:var(--white)}
.testi-title{left:369px;top:2312px;width:468px;text-align:center;font-size:38px;font-weight:700;letter-spacing:8px}
.quote{left:400px;top:2405px;width:406px;text-align:center;font-family:"Poppins",sans-serif;font-size:17px;line-height:28px;color:var(--muted)}
.avatar{left:553px;top:2519px;width:100px;height:100px;border-radius:50%;background:#cfcfcf}
.person{left:369px;top:2633px;width:468px;text-align:center;font-family:"Poppins",sans-serif;font-size:20px;font-weight:500;color:#333}
.role{left:369px;top:2667px;width:468px;text-align:center;font-family:"Poppins",sans-serif;font-size:15px;color:var(--text)}
.dots{left:582px;top:2741px;display:flex;gap:6px;align-items:center}
.dots span{width:7px;height:5px;background:#ccc}
.dots span.on{width:18px;background:var(--ink)}
.eyebrow{top:2880px;width:100%;text-align:center;font-size:10px;font-weight:700;letter-spacing:2px}
.contact-title{top:2902px;width:100%;text-align:center;font-size:26px;font-weight:500;letter-spacing:4px}
.contact-line{top:2976px;width:100%;text-align:center;font-family:"Cormorant Garamond",serif;font-size:18px;color:#666;word-spacing:2px}
.contact-line .sep{margin:0 20px}
.field{height:26px;border-bottom:1px solid #eee;font-size:10px;color:var(--text)}
.submit{left:544px;top:3246px;width:117px;height:33px;background:var(--button);color:var(--white);font-size:9.5px;font-weight:600;letter-spacing:1.5px;display:flex;align-items:center;justify-content:center}
.footer{left:0;top:3361px;width:1200px;height:81px;background:var(--band)}
.social{left:22px;top:3393px;display:flex;gap:24px;align-items:center}
.social span{width:16px;height:16px;border-radius:50%;background:#666}
.footer-link{top:3397px;font-size:9px;font-weight:700;letter-spacing:1.5px}
.copyright{right:24px;top:3396px;font-size:10px;color:var(--text)}
</style>
</head>
<body>
<header>
  <div class="abs logo">ORVANE KILN WORKS</div>
  <nav>
    <span class="abs nav" style="left:418px">Home</span>
    <span class="abs nav" style="left:512px">New Sculptures</span>
    <span class="abs nav" style="left:672px">Sold Sculptures</span>
    <span class="abs nav" style="left:835px">About</span>
    <span class="abs nav" style="left:934px">The Brindle Lads</span>
  </nav>
  <div class="abs nav-tools">
    <svg width="10" height="10" viewBox="0 0 10 10"><circle cx="4" cy="4" r="3" fill="none" stroke="#1d1d1f" stroke-width="1.2"/><line x1="6.2" y1="6.2" x2="9" y2="9" stroke="#1d1d1f" stroke-width="1.2"/></svg>
    <svg width="10" height="10" viewBox="0 0 10 10"><path d="M1 2h2l1.5 5h4l1-3.5H3.5" fill="none" stroke="#1d1d1f" stroke-width="1.1"/></svg>
  </div>
</header>

<section class="hero-section">
  <div class="abs tagline">Designed to perfection</div>
  <h1 class="abs hero-title">EXQUISITE</h1>
  <div class="abs slider-lines"><span></span><span></span><span></span></div>
  <div class="abs hero" role="img" aria-label="Amethyst geode sculpture on a wooden base against a black backdrop"></div>
</section>

<section class="new-sculptures">
  <h2 class="abs section-title" style="top:516px">NEW SCULPTURES</h2>
  <div class="abs subline"></div>
  <div class="abs subtag">CURRENT PIECES GALLERY</div>

  <div class="abs piece p-green" style="left:106px;top:723px;width:472px;height:218px" role="img" aria-label="Green jade column sculpture"></div>
  <div class="abs piece p-malachite" style="left:606px;top:723px;width:472px;height:539px" role="img" aria-label="Polished malachite sculpture on a round base"></div>
  <div class="abs piece p-blue" style="left:106px;top:970px;width:472px;height:292px" role="img" aria-label="Blue geode sculpture with purple crystal base"></div>
  <div class="abs piece p-agate" style="left:106px;top:1289px;width:224px;height:218px" role="img" aria-label="Amber agate blade sculpture"></div>
  <div class="abs piece p-lace" style="left:353px;top:1289px;width:225px;height:218px" role="img" aria-label="Blue lace agate slab sculpture"></div>
  <div class="abs piece p-ammonite" style="left:606px;top:1289px;width:222px;height:218px" role="img" aria-label="Ammonite fossil sculpture on a stand"></div>
  <div class="abs piece p-coral" style="left:851px;top:1289px;width:225px;height:218px" role="img" aria-label="Fossil coral sculpture"></div>

  <div class="abs piece p-thumb-a" style="left:106px;top:1541px;width:103px;height:104px" role="img" aria-label="Rough stone sculpture thumbnail"></div>
  <div class="abs piece p-thumb-b" style="left:239px;top:1541px;width:103px;height:104px" role="img" aria-label="Fossil coral thumbnail"></div>
  <div class="abs piece p-thumb-c" style="left:369px;top:1541px;width:103px;height:104px" role="img" aria-label="Amethyst slab thumbnail"></div>
  <div class="abs piece p-thumb-d" style="left:500px;top:1541px;width:103px;height:104px" role="img" aria-label="Golden spiral sculpture thumbnail"></div>
  <div class="abs piece p-thumb-e more" style="left:631px;top:1541px;width:103px;height:104px">
    <svg width="28" height="28" viewBox="0 0 28 28"><circle cx="14" cy="14" r="12" fill="none" stroke="#fff" stroke-width="1.5"/><path d="M14 8v12M8 14h12" stroke="#fff" stroke-width="1.5"/></svg>
  </div>
  <div class="abs piece p-thumb-f" style="left:762px;top:1541px;width:103px;height:104px" role="img" aria-label="Amethyst geode thumbnail"></div>

  <div class="abs gallery-arrows">
    <svg width="26" height="26" viewBox="0 0 26 26"><circle cx="13" cy="13" r="13" fill="#bdbdbd"/><circle cx="13" cy="13" r="6" fill="none" stroke="#fff" stroke-width="2"/></svg>
    <svg width="26" height="26" viewBox="0 0 26 26"><circle cx="13" cy="13" r="13" fill="#bdbdbd"/><circle cx="13" cy="13" r="6" fill="none" stroke="#fff" stroke-width="2"/></svg>
  </div>
</section>

<section class="about">
  <div class="abs feature" role="img" aria-label="Long arched amethyst crystal cluster"></div>
  <h2 class="abs about-title">ORVANE ART</h2>
  <p class="abs about-copy">With us you can take advantage of all the advantages of an exclusive Orvane Art Studio with personal service and expert advice. Our multi-year experience is reflected in high quality services. We firmly believe that it is better to provide a perfect service to few customers than mediocre services for many.</p>
</section>

<section class="testimonials">
  <div class="abs band"></div>
  <div class="abs quote-card"></div>
  <h2 class="abs testi-title">TESTIMONIALS</h2>
  <p class="abs quote">"Let me say something. You have an amazing theme and amazing/awesome support. They helped me on weekend. "</p>
  <div class="abs avatar"></div>
  <div class="abs person">Mara Ellison</div>
  <div class="abs role">Co-Founder / Lowfield Co</div>
  <div class="abs dots"><span></span><span class="on"></span><span></span></div>
</section>

<section class="contact">
  <div class="abs eyebrow">CONTACT</div>
  <h2 class="abs contact-title">KEEP IN TOUCH WITH US</h2>
  <div class="abs contact-line">(555) 014-2290<span class="sep">|</span>reed@brindlelads.example<span class="sep">|</span>www.orvanekilnworks.example</div>
  <div class="abs field" style="left:241px;top:3116px;width:225px">Your Name</div>
  <div class="abs field" style="left:489px;top:3116px;width:222px">Your Email</div>
  <div class="abs field" style="left:734px;top:3116px;width:218px">Your Phone</div>
  <div class="abs field" style="left:241px;top:3199px;width:711px">Your Message</div>
  <div class="abs submit">SUBMIT NOW</div>
</section>

<footer>
  <div class="abs footer"></div>
  <div class="abs social">
    <span></span><span></span><span></span><span></span>
    <svg width="18" height="14" viewBox="0 0 18 14"><rect x="0.5" y="0.5" width="17" height="13" fill="#666"/><path d="M1 1l8 7 8-7" fill="none" stroke="#f7f7f7" stroke-width="1.3"/></svg>
  </div>
  <span class="abs footer-link" style="left:453px">POLICY</span>
  <span class="abs footer-link" style="left:544px">FAQ</span>
  <span class="abs footer-link" style="left:615px">TERMS</span>
  <span class="abs footer-link" style="left:700px">SUPPORT</span>
  <span class="abs copyright">© 2018 ORVANE KILN WORKS All Rights Reserved</span>
</footer>
</body>
</html>
```